Design for Broadband Data Consumption Calculator

Primary Inspiration: http://www.quolentra-mobile.example/b2c/splash/datacalculatorPopup.jsp
This is the functionality we are looking for, but we want to use the design colors from our current site on NetKikkerten.dk
Secondary Inspiration: http://www.vimbo.dk/Privat/Mobil/Databeregner/#dc
Description
This will be a list of questions (three part, where the third part is the presentation of the price chart) that will enable us to present a list of mobile broadband providers that is suited for their needs.
Mock Up provided as well as thorough project description
Look and feel
Each slider illustrates characteristics of the customer's brand and the style your logo design should communicate.

```html
<!DOCTYPE html>
<html lang="da">
<head>
<meta charset="utf-8">
<title>NetKikkerten – Beregn dit mobilt bredbandsforbrug</title>
<link rel="stylesheet" href="https://fonts.googleapis.com/css2?family=Arimo:wght@400;700&family=Nunito:wght@700;800&display=swap">
<style>
:root{
  --teal:#2bb5ad;
  --teal-dark:#1f9a93;
  --blue:#1ea3d8;
  --blue-dark:#1580b0;
  --ink:#222;
  --muted:#8a8a8a;
  --panel:#f7f7f7;
  --line:#d4d4d4;
  --band:#ececec;
  --green:#9cc31a;
  --track:#8d8d8d;
  --footer:#d9d9d9;
}
*{box-sizing:border-box;margin:0;padding:0}
html,body{width:823px;height:1200px;overflow:hidden;background:#fff}
body{position:relative;font-family:Arimo,Arial,sans-serif;color:var(--ink)}
.abs{position:absolute}

/* header */
.site-header{left:0;top:0;width:815px;height:66px;background:var(--teal)}
.brand{left:137px;top:13px;color:#fff;font:700 17px Arimo,Arial,sans-serif}
.tagline{left:273px;top:5px;width:230px;height:16px;background:#fff;font-size:8px;line-height:16px;padding-left:6px}
.why-box{left:571px;top:5px;width:107px;height:26px;background:#fff;font-size:7.5px;font-weight:700;line-height:9px;padding:4px 0 0 20px;color:var(--ink)}
.why-box .q{position:absolute;left:3px;top:3px;font-size:18px;color:#ccc;font-weight:700}
.nav{left:133px;top:44px;width:548px;height:22px;background:#f2f2f2;display:flex;align-items:center;font-size:10.5px}
.nav span{padding:0 7px}
.nav .active{background:var(--blue);color:#fff;height:22px;line-height:22px;padding:0 9px;border-top:2px solid var(--blue-dark)}
.search{left:557px;top:47px;width:98px;height:15px;border:1px solid #999;background:#fff;font-size:7.5px;line-height:13px;padding-left:3px}
.search-btn{left:657px;top:47px;width:19px;height:15px;background:#333}

h1.title{left:0;width:823px;top:95px;text-align:center;font:800 21px Nunito,Arial,sans-serif;letter-spacing:-.3px}
.hl{color:var(--blue)}

/* steps */
.step{left:134px;width:547px;background:var(--panel);border:1px solid var(--line);border-radius:3px}
.step-num{width:24px;height:24px;border-radius:50%;background:#ddd;color:#fff;font:700 13px Arimo,sans-serif;text-align:center;line-height:24px;left:122px}
.q-text{font:700 13px Nunito,Arial,sans-serif;color:var(--ink)}
.q-text.grey{color:#8a8a8a}
.device{top:158px;height:47px;background:#e4e4e4;border:1px solid #cfcfcf;font-size:7px;text-align:center;color:#444}
.device .chk{position:absolute;width:10px;height:10px;border:1px solid #aaa;background:#f4f4f4}
.device.on{background:var(--blue);color:#fff;border-color:var(--blue-dark)}
.img-slot{background:linear-gradient(#555,#222);border-radius:3px}

.track{height:9px;border-radius:5px;background:var(--track);box-shadow:0 0 0 3px #e3e3e3}
.fill{position:absolute;left:0;top:0;height:9px;border-radius:5px;background:var(--blue)}
.knob{position:absolute;top:-3px;width:8px;height:14px;border-radius:3px;background:#ddd;border:1px solid #999}
.scale{font-size:7.5px;color:var(--muted);text-align:center;line-height:10px}
.scale b{color:var(--ink)}

.band{left:137px;width:406px;height:73px;background:var(--band)}
.use-label{font-size:8.5px;font-weight:700}
.use-label i{font-style:normal;color:var(--muted);font-weight:400}
.opts{font-size:7px;color:var(--muted);display:flex;justify-content:space-between;width:160px}
.opts b{color:var(--ink)}

.gauge{left:560px;top:413px;width:44px;height:322px;border-radius:22px;background:linear-gradient(90deg,#bdbdbd,#e0e0e0,#bdbdbd);overflow:hidden}
.gauge .lvl{position:absolute;left:0;bottom:0;width:44px;height:190px;background:linear-gradient(90deg,#1486bd,var(--blue),#1486bd)}
.gnum{left:560px;width:44px;text-align:center;font-size:10px;color:#777}
.gknob{left:556px;top:522px;width:46px;height:22px;border-radius:8px;background:linear-gradient(#fafafa,#ccc);border:1px solid #aaa}
.bubble{left:607px;top:522px;width:60px;height:56px;background:#e9e9e9;text-align:center}
.bubble .gb{display:block;background:#ddd;border:1px solid #bbb;font:700 14px Arimo,sans-serif;line-height:22px}
.bubble .lvl-t{font-size:11px;color:#999;line-height:14px;margin-top:4px;display:block}
.bubble .sub{font-size:7px;color:#aaa;display:block}
.cta{left:552px;top:720px;width:116px;height:41px;background:var(--green);color:#fff;text-align:center;border-radius:2px;padding-top:8px;font-size:10.5px;font-weight:700}
.cta small{display:block;font-size:7.5px;font-weight:400;margin-top:3px}

/* footer */
.skyline{left:0;top:985px;width:823px;height:100px;background:linear-gradient(#fff 0%,#2f7f99 35%,#2a7791 70%,#e9e9e9 100%)}
.site-footer{left:137px;top:1065px;width:539px;height:135px;background:var(--footer);border:1px solid #c4c4c4}
.fcol-h{font:700 13px Arimo,sans-serif;color:#333}
.fsmall{font-size:6.5px;line-height:8.5px;color:#222}
.list{list-style:none;font-size:6.5px;line-height:12px}
.list li::before{content:"›  ";color:#888}
</style>
</head>
<body>

<header class="abs site-header"></header>
<div class="abs brand">NetKikkerten</div>
<div class="abs tagline">Aktuelle prisoversigter og gratis hjælp, når du skal finde nyt bredbånd</div>
<div class="abs why-box"><span class="q">?</span>Hvorfor skal jeg bruge netkikkerten?</div>
<nav class="abs nav">
  <span class="active">Forsiden</span><span>Prisoversigter ▾</span><span>Anmeldelser ▾</span><span>Artikler</span><span>Hastighedsguide</span><span>● Om Os</span>
</nav>
<div class="abs search">Søgefelt...</div>
<div class="abs search-btn"></div>

<h1 class="abs title">Beregn <span class="hl">dit mobilt</span> bredbandsforbrug i <span class="hl">3 enkle</span> skridt</h1>

<!-- step 1 -->
<div class="abs step" style="top:151px;height:62px"></div>
<div class="abs step-num" style="top:140px">1</div>
<div class="abs q-text" style="left:147px;top:165px;line-height:16px">What <span class="hl">device</span> do you need<br><span class="hl">mobile broadband</span> for?</div>
<div class="abs" style="left:321px;top:152px;width:1px;height:60px;background:var(--line)"></div>

<div class="abs device" style="left:342px;width:69px"><div class="img-slot abs" role="img" aria-label="Smartphone" style="left:8px;top:5px;width:14px;height:36px"></div><span class="chk" style="left:44px;top:7px"></span><span class="abs" style="left:36px;top:24px">Smart<br>Phone</span></div>
<div class="abs img-slot" role="img" aria-label="Tablet" style="left:421px;top:147px;width:40px;height:60px"></div>
<div class="abs device on" style="left:459px;width:38px"><span class="chk" style="left:13px;top:7px;background:#fff"></span><span class="abs" style="left:8px;top:24px">Tablet</span></div>
<div class="abs device" style="left:513px;width:70px"><span class="chk" style="left:44px;top:7px"></span><span class="abs" style="left:36px;top:24px">PC With<br>router</span></div>
<div class="abs img-slot" role="img" aria-label="Laptop" style="left:505px;top:172px;width:42px;height:38px;background:linear-gradient(#8ab,#ccc)"></div>
<div class="abs device" style="left:598px;width:70px"><div class="img-slot abs" role="img" aria-label="Several devices" style="left:2px;top:10px;width:32px;height:30px;background:linear-gradient(#9bc,#ddd)"></div><span class="chk" style="left:46px;top:7px"></span><span class="abs" style="left:36px;top:24px">Multiple<br>devices</span></div>

<!-- step 2 -->
<div class="abs step" style="top:236px;height:107px"></div>
<div class="abs step-num" style="top:226px">2</div>
<div class="abs" role="img" aria-label="Alarm clock" style="left:147px;top:246px;width:20px;height:20px;border-radius:50%;background:#e05a20"></div>
<div class="abs q-text grey" style="left:175px;top:250px">Essentials: <span class="hl">How often are you online?</span></div>
<div class="abs track" style="left:145px;top:285px;width:523px"><span class="fill" style="width:198px"></span><span class="knob" style="left:195px"></span></div>
<div class="abs scale" style="left:160px;top:307px;width:90px">A couple of times<br>a week or less..</div>
<div class="abs scale" style="left:302px;top:307px;width:80px"><b>Every day..</b></div>
<div class="abs scale" style="left:440px;top:307px;width:80px">Multiple times<br>a day</div>
<div class="abs scale" style="left:576px;top:307px;width:80px">Online all day</div>

<!-- step 3 -->
<div class="abs step" style="top:369px;height:405px"></div>
<div class="abs step-num" style="top:359px">3</div>
<div class="abs" role="img" aria-label="Globe" style="left:147px;top:381px;width:20px;height:20px;border-radius:50%;background:radial-gradient(#9fd4ef,#2a7fb4)"></div>
<div class="abs q-text grey" style="left:175px;top:383px">Details: <span class="hl">What are you going to use your mobile broadband for?</span></div>

<div class="abs band" style="top:477px"></div>
<div class="abs band" style="top:626px"></div>

<!-- rows -->
<div class="abs use-label" style="left:160px;top:417px">Surfing, reading articles, netbanking</div>
<div class="abs use-label" style="left:364px;top:417px">Sending e-mails <i>(with photos)</i></div>
<div class="abs use-label" style="left:160px;top:491px">Social media <i>(Venneside, Kvidr, etc.)</i></div>
<div class="abs use-label" style="left:364px;top:491px">Sending e-mails <i>(without photos)</i></div>
<div class="abs use-label" style="left:160px;top:565px">Watching videos online <i>(Klipzone, TV-Nu.dk,..)</i></div>
<div class="abs use-label" style="left:364px;top:565px">Listening to music online</div>
<div class="abs use-label" style="left:160px;top:640px">Download smaller files <i>(below 50 MB)</i></div>
<div class="abs use-label" style="left:364px;top:640px">Play online video games</div>
<div class="abs use-label" style="left:160px;top:714px">Download medium files <i>(50 - 100 MB)</i></div>
<div class="abs use-label" style="left:364px;top:714px">Download large files <i>(over 100 MB)</i></div>

<div class="abs track" style="left:148px;top:434px;width:179px"><span class="fill" style="width:24px"></span><span class="knob" style="left:20px"></span></div>
<div class="abs track" style="left:351px;top:434px;width:183px"><span class="fill" style="width:24px"></span><span class="knob" style="left:20px"></span></div>
<div class="abs track" style="left:148px;top:508px;width:179px"><span class="fill" style="width:24px"></span><span class="knob" style="left:20px"></span></div>
<div class="abs track" style="left:351px;top:508px;width:183px"><span class="fill" style="width:24px"></span><span class="knob" style="left:20px"></span></div>
<div class="abs track" style="left:148px;top:582px;width:179px"><span class="fill" style="width:24px"></span><span class="knob" style="left:20px"></span></div>
<div class="abs track" style="left:351px;top:582px;width:183px"><span class="fill" style="width:24px"></span><span class="knob" style="left:20px"></span></div>
<div class="abs track" style="left:148px;top:656px;width:179px"><span class="fill" style="width:24px"></span><span class="knob" style="left:20px"></span></div>
<div class="abs track" style="left:351px;top:656px;width:183px"><span class="fill" style="width:24px"></span><span class="knob" style="left:20px"></span></div>
<div class="abs track" style="left:148px;top:731px;width:179px"><span class="fill" style="width:24px"></span><span class="knob" style="left:20px"></span></div>
<div class="abs track" style="left:351px;top:731px;width:183px"><span class="fill" style="width:24px"></span><span class="knob" style="left:20px"></span></div>

<div class="abs opts" style="left:161px;top:452px"><b>Never</b><span>Sometimes</span><span>Often</span></div>
<div class="abs opts" style="left:364px;top:452px"><b>Never</b><span>Sometimes</span><span>Often</span></div>
<div class="abs opts" style="left:161px;top:526px"><b>Never</b><span>Sometimes</span><span>Often</span></div>
<div class="abs opts" style="left:364px;top:526px"><b>Never</b><span>Sometimes</span><span>Often</span></div>
<div class="abs opts" style="left:161px;top:600px"><b>Never</b><span>Sometimes</span><span>Often</span></div>
<div class="abs opts" style="left:364px;top:600px"><b>Never</b><span>Sometimes</span><span>Often</span></div>
<div class="abs opts" style="left:161px;top:675px"><b>Never</b><span>Sometimes</span><span>Often</span></div>
<div class="abs opts" style="left:364px;top:675px"><b>Never</b><span>Sometimes</span><span>Often</span></div>
<div class="abs opts" style="left:161px;top:749px"><b>Never</b><span>Sometimes</span><span>Often</span></div>
<div class="abs opts" style="left:364px;top:749px"><b>Never</b><span>Sometimes</span><span>Often</span></div>

<!-- gauge -->
<div class="abs gauge"><span class="lvl"></span></div>
<div class="abs gnum" style="top:432px">21</div>
<div class="abs gnum" style="top:487px">15</div>
<div class="abs gnum" style="top:549px;color:#cde">10</div>
<div class="abs gnum" style="top:610px;color:#cde">5</div>
<div class="abs gnum" style="top:670px;color:#cde">0</div>
<div class="abs gknob"></div>
<div class="abs bubble"><span class="gb">13GB</span><span class="lvl-t">High</span><span class="sub">consumption</span></div>
<div class="abs cta">Sammenlign priser på<small>15GB mobilt bredbånd</small></div>

<!-- footer -->
<div class="abs skyline" role="img" aria-label="City skyline above clouds"></div>
<footer class="abs site-footer"></footer>
<div class="abs fcol-h" style="left:174px;top:1073px">Om NetKikkerten</div>
<div class="abs fcol-h" style="left:343px;top:1073px">Sidste Kommentarer</div>
<div class="abs fcol-h" style="left:520px;top:1073px">Seneste Nyheder</div>
<div class="abs fsmall" style="left:178px;top:1106px"><b>NetKikkerten.dk</b> drives af:<br>Ravnlund ApS<br>Egetoften 7B<br>9999 Lunddal<br><br>CVR: 00000000<br>Tlf.: 00 00 00 00</div>
<ul class="abs list" style="left:337px;top:1106px">
  <li>Hej Jonas, De skal ikke betale. Der e ...</li>
  <li>Hej igen Nu har jeg fået installeret 3 ...</li>
  <li>Hej Mette, Hvis du oplyser hvilken by d ...</li>
  <li>Hej Jeg bor også på landet og kan se ...</li>
  <li>Hej Lise, Det billigste jeg kunne find ...</li>
</ul>
<ul class="abs list" style="left:502px;top:1106px;width:160px">
  <li>Hvad er det bedste Nordlyn alternativ?</li>
  <li>Hjælp til kunder efter Nordlyn konkurs</li>
  <li style="line-height:10px">Hvilke kendetegn har de gode internet udbydere til fælles?</li>
  <li style="line-height:10px">Skjulte faktorer du sikkert ikke måler billig internet på</li>
  <li>Sådan finder du ud af om billig bredbånd er for dig</li>
</ul>

</body>
</html>
```